House-share and Room Rental Website (With Focus on the Bedroom Landing Page)

Looking for website design for our House-share (executive accommodation) and room rental business.

Our company name is: Lodvenra could also be written as LodVenra or lodvenra. Either is fine .. just looking for a nice clean catchy logo to go with the design.

EXAMPLES
These are examples of other websites in this field that are doing well. this is a kind of baseline.
https://kelbrin.com.au/
https://www.tuvaplex.com/
https://www.nestorvi.com/
https://www.quillsa.net/
https://www.pendlebarrow.com.au/

Our business model is to rent rooms to people looking for high-quality accommodation. We fill the gap between those looking to rent rooms and those with rooms to rent. However, our model is slightly different from those already on the market as we looking to fill a massive gap in the market delivering upmarket rooms for rent.(Executive Accommodation) also in the back end will be coupled with a self management process in the back end.

We offer executive style accommodation that stands out above the rest. With special extras like fire safety.. and management processes that create happier homes. We are looking for a web design package that can help us grow and scale our business. We need a design that is captivating

Our MAIN focus is having a room landing page that stands out from the rest... The core of our business will rely on the promotion of the rooms in a share house... so the whole design relies on the BEDROOM landing page to drive results.

Target Market(s)

We have 2 markets we are aiming at ... the first market is people offering rooms to rent who want the highest rental return. The second market is people looking to rent safe, high-quality rooms, in houses that are well managed and looked after.

Industry/Entity Type

Share Economy

Logo Text

LodVenra

Number of Pages Required

5+ page

Font styles to use
Sans Serif

Colors
3276b5

Requirements
Must have
• A messaging system whereby we can create direct communication between those offering rooms and those looking for rooms.
• A call to action that says " Schedule an Inspection"
• Landing page for promoting rooms
• A home page for showing stock.
• Profile page for those selling rooms
• Profile page for those looking for rooms.
• A scheduling calendar for booking inspections
Nice to have
• Pages where new residents can lock in a room.. pay bond and rents.. and sign contracts
• Notifications
• SMS capabilities in the backend.
Should not have
• No script or handwriting fonts.

```html
<!DOCTYPE html>
<html lang="en">
<head>
<meta charset="utf-8">
<title>LodVenra – The white room</title>
<link href="https://fonts.googleapis.com/css2?family=Lato:wght@300;400;700;900&display=swap" rel="stylesheet">
<style>
:root{
  --blue:#3276b5;
  --ink:#1c1c1c;
  --text:#2b2b2b;
  --muted:#8f8f8f;
  --faint:#c9c9c9;
  --line:#e2e2e2;
  --star-off:#c8c8c8;
  --bed-light:#dcd8d3;
  --bed-mid:#b9b2aa;
  --bed-dark:#8b8179;
}
*{box-sizing:border-box;margin:0;padding:0}
html,body{width:880px;height:1200px;overflow:hidden;background:#fff}
body{position:relative;font-family:'Lato',sans-serif;color:var(--text)}
.abs{position:absolute}

/* header */
.brand{left:22px;top:24px;display:flex;align-items:center;gap:6px;font-weight:900;font-size:15px;color:var(--blue)}
.brand-mark{width:10px;height:10px;background:var(--blue)}
.nav{top:26px;right:0;left:0;height:14px}
.nav a{position:absolute;font-size:7.5px;font-weight:700;letter-spacing:.8px;color:var(--ink);text-decoration:none;top:1px}
.nav .sep{position:absolute;width:1px;height:7px;background:var(--ink);top:3px}
.signin{left:795px;top:19px;width:63px;height:23px;border:1px solid #333;border-radius:2px;font-size:7.5px;font-weight:700;letter-spacing:.8px;color:var(--blue);display:flex;align-items:center;justify-content:center}

/* gallery */
.photo{background:linear-gradient(160deg,var(--bed-light),var(--bed-mid) 60%,var(--bed-dark))}
.photo-main{left:12px;top:66px;width:422px;height:324px;background:linear-gradient(180deg,#d6d2cb 0%,#b3aaa0 45%,#eceae7 70%,#d9d6d2 100%)}
.photo-wide{left:446px;top:66px;width:422px;height:156px;background:linear-gradient(180deg,#a9a29b,#d8d4cf 60%,#c5bdb4)}
.photo-vase{left:446px;top:234px;width:205px;height:156px;background:linear-gradient(180deg,#e3e1df 0%,#c9c6c2 60%,#5a514b 80%,#efeeec 100%)}
.photo-pillow{left:663px;top:234px;width:205px;height:156px;background:linear-gradient(170deg,#d4d0cc,#aaa39c 60%,#e6e3e0)}

/* room info */
.city{font-size:10px;font-weight:700;letter-spacing:.2px;color:var(--ink)}
.room-title{left:153px;top:424px;font-size:29px;font-weight:300;color:var(--ink)}
.room-type{left:153px;top:460px;font-size:15px;font-weight:900;color:var(--ink)}
.rating{display:flex;align-items:center;gap:2px;font-size:8.5px;color:var(--ink)}
.rating svg{width:10px;height:10px;fill:var(--blue)}
.rating svg.off{fill:var(--star-off)}
.rating span{margin-left:3px}
.desc{left:153px;top:510px;width:285px;font-size:11.3px;line-height:14.7px;color:var(--ink)}
.location{left:153px;top:604px;display:flex;align-items:center;gap:15px}
.location h3{font-size:15px;font-weight:900;color:var(--ink)}
.location p{font-size:11px;color:var(--ink);display:flex;align-items:center;gap:6px}

/* price */
.price-label{left:446px;top:411px;font-size:8px;color:var(--ink)}
.price{left:446px;top:422px;font-size:26px;font-weight:700;color:var(--blue)}
.book{left:593px;top:426px;width:134px;height:21px;background:var(--blue);color:#fff;font-size:8px;letter-spacing:.6px;display:flex;align-items:center;justify-content:center}

.section-title{font-size:15px;font-weight:900;color:var(--ink)}
.feature{width:70px;margin-left:-35px;text-align:center}
.feature svg{width:13px;height:13px;stroke:#333;fill:none;stroke-width:1.1;display:block;margin:0 auto}
.feature .cap{font-size:3.6px;color:var(--faint);letter-spacing:.3px;text-transform:uppercase;margin-top:1px}
.feature .val{font-size:7px;color:var(--ink);margin-top:1px}

/* amenities */
.amenity{width:90px;margin-left:-45px;text-align:center}
.amenity svg{width:26px;height:22px;stroke:#444;fill:none;stroke-width:1;display:block;margin:0 auto}
.amenity p{font-size:9.5px;color:var(--ink);margin-top:4px}

.transport{left:446px;width:140px;display:flex;align-items:center}
.transport svg.ico{width:16px;height:13px;stroke:#555;fill:none;stroke-width:1;margin-right:10px}
.transport strong{font-size:9.5px;font-weight:700;color:var(--ink);flex:1}
.transport svg.chev{width:8px;height:6px;stroke:var(--ink);fill:none;stroke-width:1.3}
.transport-sub{left:472px;top:697px;font-size:7.5px;color:var(--ink)}

/* similar */
.card{width:183px}
.card-img{width:183px;height:103px}
.card .city{color:var(--blue);font-weight:400;font-size:9px;margin-top:14px}
.card h4{font-size:18px;font-weight:300;color:var(--ink);margin-top:3px;line-height:20px}
.card h5{font-size:12px;font-weight:900;color:var(--ink);line-height:14px}
.card .rating{margin-top:3px}

/* footer */
.footer-line{left:153px;top:1102px;width:574px;height:1px;background:var(--line)}
.footer-brand{left:153px;top:1110px;display:flex;align-items:center;gap:5px;font-weight:900;font-size:14px;color:var(--muted)}
.footer-brand i{width:9px;height:9px;background:var(--muted)}
.footer-col{top:1109px;list-style:none;font-size:10.5px;line-height:18.5px;color:var(--muted)}
</style>
</head>
<body>

<svg width="0" height="0" style="position:absolute">
  <symbol id="star" viewBox="0 0 20 20"><polygon points="10,1 12.6,7.3 19.4,7.6 14.1,11.9 15.9,18.6 10,14.8 4.1,18.6 5.9,11.9 0.6,7.6 7.4,7.3"/></symbol>
  <symbol id="chev" viewBox="0 0 8 6"><polyline points="1,1.5 4,4.5 7,1.5"/></symbol>
</svg>

<!-- header -->
<header>
  <div class="abs brand"><span class="brand-mark"></span>LodVenra</div>
  <nav class="abs nav">
    <a style="left:495px">BROWSE</a>
    <a style="left:553px">DISCOVER</a>
    <span class="sep" style="left:620px"></span>
    <a style="left:641px">LIST YOUR FLAT</a>
    <span class="sep" style="left:732px"></span>
    <a style="left:753px">LOGIN</a>
  </nav>
  <div class="abs signin">SIGN IN</div>
</header>

<!-- gallery -->
<div class="abs photo-main" role="img" aria-label="White bedroom with double bed, grey pillows, wooden breakfast tray and pendant lights"></div>
<div class="abs photo-wide" role="img" aria-label="Close-up of pillows and breakfast tray with white flowers"></div>
<div class="abs photo-vase" role="img" aria-label="Grey ceramic ring vase on a dark bedside table"></div>
<div class="abs photo-pillow" role="img" aria-label="Quilted headboard and grey cushion detail"></div>

<!-- room info -->
<div class="abs city" style="left:153px;top:411px">MELBOURNE</div>
<h1 class="abs room-title">The white room</h1>
<h2 class="abs room-type">DOUBLE BEDROOM</h2>
<div class="abs rating" style="left:153px;top:484px">
  <svg><use href="#star"/></svg><svg><use href="#star"/></svg><svg><use href="#star"/></svg><svg><use href="#star"/></svg><svg><use href="#star"/></svg><span>314</span>
</div>
<p class="abs desc">Maecenas et ligula consectetur diam convallis posuere eget eget velit. Morbi ac augue at dolor sollicitudin rhoncus. Cras vulputate, metus at iaculis varius, tellus nisl scelerisque magna, vel consectetur elit mi id nisi. Ut blandit orci vel lectus sagittis, nec fermentum neque fringilla.</p>
<div class="abs location">
  <h3>Location</h3>
  <p>Larkin Crescent, ELMSWORTH HEIGHTS <svg width="8" height="6" style="stroke:var(--ink);fill:none;stroke-width:1.3"><use href="#chev"/></svg></p>
</div>

<!-- price & features -->
<div class="abs price-label">Rental price (per month)</div>
<div class="abs price">A$600</div>
<div class="abs book">BOOK</div>

<h3 class="abs section-title" style="left:446px;top:472px">Features</h3>

<div class="abs feature" style="left:468px;top:502px"><svg viewBox="0 0 14 14"><circle cx="7" cy="4.5" r="3"/><path d="M1.5 13c0-3 2.5-5 5.5-5s5.5 2 5.5 5"/></svg><div class="cap">Gender</div><div class="val">Single</div></div>
<div class="abs feature" style="left:530px;top:502px"><svg viewBox="0 0 14 14"><rect x="3" y="1" width="8" height="12"/><path d="M5 1v12"/></svg><div class="cap">Room size</div><div class="val">40 Sqm</div></div>
<div class="abs feature" style="left:591px;top:502px"><svg viewBox="0 0 14 14"><path d="M2 2h4v6H2zM2 8h10l-2 3H5v2"/></svg><div class="cap">Bathroom</div><div class="val">Private</div></div>
<div class="abs feature" style="left:650px;top:502px"><svg viewBox="0 0 14 14"><rect x="1.5" y="1.5" width="11" height="11"/><path d="M5.5 10.5v-7h2.5a2 2 0 0 1 0 4H5.5"/></svg><div class="cap">Parking</div><div class="val">Private</div></div>
<div class="abs feature" style="left:707px;top:502px"><svg viewBox="0 0 14 14"><circle cx="7" cy="7" r="5.5"/><path d="M3 11L11 3M4 8h5"/></svg><div class="cap">Smoking</div><div class="val">Not allowed</div></div>

<div class="abs feature" style="left:468px;top:548px"><svg viewBox="0 0 14 14"><path d="M11 7v5H2V3h5"/><path d="M5 9l1-3 6-5 2 2-6 5z"/></svg><div class="cap">Minimum contract</div><div class="val">3 months</div></div>
<div class="abs feature" style="left:530px;top:548px"><svg viewBox="0 0 14 14"><rect x="2" y="2" width="10" height="9"/><path d="M2 7h10M2 11v2M12 11v2M4 4h6v3H4z"/></svg><div class="cap">Bed size</div><div class="val">200x200</div></div>
<div class="abs feature" style="left:591px;top:548px"><svg viewBox="0 0 14 14"><circle cx="4.5" cy="5" r="2.5"/><circle cx="9.5" cy="5" r="2.5"/><path d="M0.5 12c0-2.5 2-4 4-4s4 1.5 4 4M5.5 12c0-2.5 2-4 4-4s4 1.5 4 4"/></svg><div class="cap">Housemates</div><div class="val">Professionals</div></div>
<div class="abs feature" style="left:650px;top:548px"><svg viewBox="0 0 14 14"><rect x="3.5" y="1" width="7" height="12"/><circle cx="8.5" cy="7" r=".6"/></svg><div class="cap">Room type</div><div class="val">Private</div></div>
<div class="abs feature" style="left:707px;top:548px"><svg viewBox="0 0 14 14"><path d="M1.5 6a8 8 0 0 1 11 0M3.5 8.2a5 5 0 0 1 7 0M5.5 10.3a2 2 0 0 1 3 0"/><circle cx="7" cy="12" r=".5"/></svg><div class="cap">Internet speed</div><div class="val">600mbps</div></div>

<!-- amenities -->
<h3 class="abs section-title" style="left:153px;top:652px">Amenities</h3>

<div class="abs amenity" style="left:174px;top:678px"><svg viewBox="0 0 26 22"><path d="M3 8h20v8H3zM1 10h2v8M23 10h2v8M1 18h24M5 8V5h16v3"/></svg><p>Furnished</p></div>
<div class="abs amenity" style="left:234px;top:678px"><svg viewBox="0 0 26 22"><rect x="2" y="2" width="22" height="16" rx="4"/><path d="M10 21h6"/><text x="13" y="13" font-size="7" text-anchor="middle" fill="#444" stroke="none" font-family="Lato,sans-serif">TV</text></svg><p>SmartTV</p></div>
<div class="abs amenity" style="left:303px;top:678px"><svg viewBox="0 0 26 22"><rect x="6" y="1" width="14" height="20"/><path d="M6 6h14M6 11h14M6 16h14M9 3h3M14 8h3M9 13h4"/></svg><p>Storage space</p></div>
<div class="abs amenity" style="left:379px;top:678px"><svg viewBox="0 0 26 22"><path d="M2 13h22M4 13v8M22 13v8M4 16h6M14 4h8v6h-8zM18 10v3M6 5h5v8H6z"/></svg><p>Workstation</p></div>

<div class="abs amenity" style="left:174px;top:736px"><svg viewBox="0 0 26 22"><rect x="4" y="1" width="18" height="20"/><path d="M13 1v12M4 13h18M4 17h18M11 6v3M15 6v3"/></svg><p>Wardrobe</p></div>
<div class="abs amenity" style="left:249px;top:736px"><svg viewBox="0 0 26 22"><path d="M3 12h20v4a3 3 0 0 1-3 3H6a3 3 0 0 1-3-3zM17 12V4a2 2 0 0 1 4 0M8 12V9h4v3M6 19v2M20 19v2"/></svg><p>Ensuite shower</p></div>
<div class="abs amenity" style="left:327px;top:736px"><svg viewBox="0 0 26 22"><path d="M1 10h24v11H1zM9 10v11M17 10v11M3 2h20M5 2v5M10 2v5M16 2v5M21 2v5M3 14h4M11 13h4v4h-4z"/></svg><p>Kitchenette</p></div>

<!-- public amenities -->
<h3 class="abs section-title" style="left:446px;top:652px">Public Amenities</h3>

<div class="abs transport" style="top:680px"><svg class="ico" viewBox="0 0 16 13"><path d="M1 6.5h14M6 6.5L3 1h2l4 5.5M6 6.5L3 12h2l4-5.5M1 6.5L0.5 4M13 6.5c1 0 2 .3 2 .3"/></svg><strong>Distance to the airport</strong></div>
<div class="abs transport-sub">15 minutes by car</div>
<div class="abs transport" style="top:719px"><svg class="ico" viewBox="0 0 16 13"><rect x="3" y="0.5" width="10" height="11" rx="1"/><path d="M3 6h10M5 11.5v1M11 11.5v1M5 3h6"/></svg><strong>Busses</strong><svg class="chev"><use href="#chev"/></svg></div>
<div class="abs transport" style="top:743px"><svg class="ico" viewBox="0 0 16 13"><rect x="2" y="0.5" width="12" height="10" rx="1"/><path d="M2 6h12M4 12.5l1.5-2M12 12.5l-1.5-2"/></svg><strong>Trains</strong><svg class="chev"><use href="#chev"/></svg></div>
<div class="abs transport" style="top:768px"><svg class="ico" viewBox="0 0 16 13"><path d="M1 6h14v4H1zM3 6l2-4h6l2 4M3 10v2M13 10v2"/><circle cx="4" cy="8" r=".6"/><circle cx="12" cy="8" r=".6"/></svg><strong>Rent a car</strong><svg class="chev"><use href="#chev"/></svg></div>

<!-- similar bedrooms -->
<h3 class="abs section-title" style="left:153px;top:850px">Similar Bedrooms</h3>

<article class="abs card" style="left:153px;top:878px">
  <div class="card-img" role="img" aria-label="Warm hotel-style bedroom with olive bedspread" style="background:linear-gradient(180deg,#5f5640,#8b7a5a 50%,#c9b89a)"></div>
  <div class="city">MELBOURNE</div>
  <h4>Luxury in the mountains</h4>
  <h5>DOUBLE BEDROOM</h5>
  <div class="rating"><svg><use href="#star"/></svg><svg><use href="#star"/></svg><svg><use href="#star"/></svg><svg><use href="#star"/></svg><svg class="off"><use href="#star"/></svg><span>180</span></div>
</article>

<article class="abs card" style="left:348px;top:878px">
  <div class="card-img" role="img" aria-label="Dark wood bedroom with white bedding and red cushions" style="background:linear-gradient(180deg,#3a2226,#6b3b40 45%,#e5e2e0 75%,#7a7478)"></div>
  <div class="city">MELBOURNE</div>
  <h4>Cherry room</h4>
  <h5>DOUBLE BEDROOM</h5>
  <div class="rating"><svg><use href="#star"/></svg><svg><use href="#star"/></svg><svg><use href="#star"/></svg><svg><use href="#star"/></svg><svg><use href="#star"/></svg><span>215</span></div>
</article>

<article class="abs card" style="left:544px;top:878px">
  <div class="card-img" role="img" aria-label="Bedroom with stone feature wall and blue bed on pallet base" style="background:linear-gradient(180deg,#4a4642,#6e6660 50%,#5b78a8 75%,#cbb89a)"></div>
  <div class="city">MELBOURNE</div>
  <h4>The wall</h4>
  <h5>DOUBLE BEDROOM</h5>
  <div class="rating"><svg><use href="#star"/></svg><svg><use href="#star"/></svg><svg><use href="#star"/></svg><svg><use href="#star"/></svg><svg><use href="#star"/></svg><span>432</span></div>
</article>

<!-- footer -->
<footer>
  <div class="abs footer-line"></div>
  <div class="abs footer-brand"><i></i>LodVenra</div>
  <ul class="abs footer-col" style="left:299px"><li>Paid methods</li><li>Cancellation policy</li><li>Other</li></ul>
  <ul class="abs footer-col" style="left:446px"><li>Conditions</li><li>Be a Landlor</li><li>Selling rooms</li></ul>
  <ul class="abs footer-col" style="left:593px"><li>Terms</li><li>Privacity</li><li>Sitemap</li></ul>
</footer>

</body>
</html>
```